Rack Card Design for an Ayurvedic Beauty Product Project

Hello, I need to have rack cards. The rack cards would be about 3 products we are showcasing at an event. I am a cosmetic company. I have a logo and basic design ideas. I have attached some product images and info. By no means am I a designer so please excuse my messy AI files. Please feel free to design this as feminine as you like. :)

Target Market(s)

Beauty industry, organic, holistic, ayurveda

Industry/Entity Type

Cosmetic

```html
<!DOCTYPE html>
<html lang="en">
<head>
<meta charset="utf-8">
<title>Amber Petal Rack Cards</title>
<link href="https://fonts.googleapis.com/css2?family=Quicksand:wght@400;500;600;700&display=swap" rel="stylesheet">
<style>
:root{
  --page:#5f5f5f;
  --cream:#f6efdc;
  --cream-light:#fbf7ee;
  --white:#ffffff;
  --plum:#6c1d52;
  --plum-text:#74205a;
  --gold:#b48c55;
  --gold-light:#dcc08e;
  --ink:#3a3a3a;
}
*{box-sizing:border-box;margin:0;padding:0}
html,body{width:1200px;height:1200px;overflow:hidden}
body{background:var(--page);font-family:"Quicksand",sans-serif;color:var(--ink);position:relative}
.card{position:absolute;top:121px;width:440px;height:958px;overflow:hidden;
  background:linear-gradient(180deg,var(--cream) 0%,var(--cream-light) 48%,var(--white) 62%,var(--white) 100%)}
.card--intro{left:140px}
.card--list{left:620px}
.card--list{background:linear-gradient(180deg,var(--cream) 0%,var(--cream-light) 25%,var(--white) 45%,var(--white) 100%)}
.photo{position:absolute;border-radius:4px}
.photo--portrait{left:18px;top:25px;width:230px;height:405px;
  background:radial-gradient(ellipse at 45% 40%,#f1d3c0 0%,#e8c3ac 45%,rgba(240,225,205,0) 75%)}
.photo--products{left:40px;top:330px;width:400px;height:230px;
  background:radial-gradient(ellipse at 50% 55%,#e7c766 0%,#dca56a 35%,#d98a78 55%,rgba(250,245,235,0) 78%)}
.brand{position:absolute;display:flex;flex-direction:column;align-items:center;gap:14px}
.brand__dot{width:78px;height:78px;border-radius:50%;background:var(--gold)}
.brand__name{font-weight:700;font-size:17px;letter-spacing:.5px;color:var(--gold)}
.card--intro .brand{left:230px;top:62px;width:170px}
.card--list .brand{left:120px;top:44px;width:200px}
.intro__title{position:absolute;left:0;width:440px;top:588px;text-align:center;
  font-weight:700;font-size:41px;letter-spacing:1px;color:var(--gold)}
.intro__sub{position:absolute;left:34px;top:636px;font-weight:700;font-size:21.5px;color:var(--plum-text)}
.intro__body{position:absolute;left:34px;top:667px;width:372px;font-size:14.4px;line-height:18.1px;
  text-align:justify;font-weight:500}
.footer{position:absolute;left:0;bottom:0;width:440px;height:110px}
.footer svg{position:absolute;left:0;top:0}
.contact{position:absolute;left:0;bottom:14px;width:440px;display:flex;justify-content:center;gap:26px;
  color:var(--white);font-size:17.5px;font-weight:500}
.contact span{display:flex;align-items:center;gap:7px}
.contact .phone{font-size:18.5px}
.list__head{position:absolute;left:26px;top:196px;width:388px;height:32px}
.list__head::before{content:"";position:absolute;left:0;right:0;top:16px;height:1px;background:var(--plum)}
.list__pill{position:absolute;left:38px;top:0;width:312px;height:32px;border-radius:16px;background:var(--plum);
  color:var(--gold-light);font-weight:700;font-size:20px;letter-spacing:.5px;text-align:center;line-height:32px}
.product__img{position:absolute;left:25px;width:111px;
  background:radial-gradient(ellipse at 50% 55%,var(--c1) 0%,var(--c2) 45%,rgba(255,255,255,0) 75%)}
.product__img--toner{top:252px;height:190px;--c1:#e57a6a;--c2:#eab2a5}
.product__img--cream{top:488px;height:107px;--c1:#ecd05a;--c2:#c98aa9}
.product__img--serum{top:646px;height:190px;--c1:#d9a43a;--c2:#ecd39a}
.product__text{position:absolute;left:168px;width:244px}
.product__name{font-size:18px;line-height:21px;font-weight:500;color:var(--plum-text);margin-bottom:6px}
.product__desc{font-size:14.4px;line-height:18.1px;text-align:justify;font-weight:500}
.product__text--toner{top:294px}
.product__text--cream{top:484px}
.product__text--serum{top:649px}
</style>
</head>
<body>

<section class="card card--intro">
  <div class="photo photo--portrait" role="img" aria-label="Portrait photo of a woman with smooth skin and hair pulled back"></div>
  <div class="photo photo--products" role="img" aria-label="Product photo of a gold cream jar, a gold-flake serum bottle and a rose toner dropper bottle"></div>
  <div class="brand"><span class="brand__dot"></span><span class="brand__name">AMBER PETAL</span></div>
  <h1 class="intro__title">AMBER PETAL</h1>
  <p class="intro__sub">curates organic infused products</p>
  <p class="intro__body">Amber Petal curates organic infused products where holistic skin care meets a luxurious experience. Each ingredient is carefully selected; providing Ayurvedic herbs, rich minerals and elements. Stimulating hydration and anti-oxidants to lift, firm and illuminate your skin. We believe in connecting with your inner mantra, stimulating higher vibrations, self-esteem, positive mind and soul. As a brand we work with our experts/suppliers of Ayurveda to ensure that our products meet the quality, wholesome healing that you need.</p>
  <div class="footer">
    <svg width="440" height="110" viewBox="0 0 440 110">
      <path d="M0 14 Q220 62 440 38 L440 110 L0 110 Z" fill="var(--gold-light)"/>
      <path d="M0 26 Q220 66 440 42 L440 110 L0 110 Z" fill="var(--plum)"/>
    </svg>
    <div class="contact">
      <span class="phone"><svg width="16" height="16" viewBox="0 0 16 16"><circle cx="8" cy="8" r="7" fill="none" stroke="#fff" stroke-width="1.2"/><path d="M5.3 4.5l1.3 0 .5 1.6-.8.7c.4.9 1 1.5 1.9 1.9l.7-.8 1.6.5 0 1.3c-3 .3-5.5-2.2-5.2-5.2z" fill="#fff"/></svg>555 010 2040</span>
      <span><svg width="16" height="16" viewBox="0 0 16 16" fill="none" stroke="#fff" stroke-width="1.1"><circle cx="8" cy="8" r="6.5"/><ellipse cx="8" cy="8" rx="2.8" ry="6.5"/><path d="M1.5 8h13M2.5 5h11M2.5 11h11"/></svg>www.amberpetal.com</span>
    </div>
  </div>
</section>

<section class="card card--list">
  <div class="brand"><span class="brand__dot"></span><span class="brand__name">AMBER PETAL</span></div>
  <div class="list__head"><div class="list__pill">AMBER PETAL PRODUCT LIST</div></div>

  <div class="product__img product__img--toner" role="img" aria-label="Photo of the rose-coloured breast toner dropper bottle"></div>
  <div class="product__text product__text--toner">
    <h2 class="product__name">Amber Petal Firming and Lifting Breast Toner</h2>
    <p class="product__desc">Using all natural Ayurvedic herbs, our breast toner,prepares the area for maximum absorption, giving you the best results and the most invigorating treatment</p>
  </div>

  <div class="product__img product__img--cream" role="img" aria-label="Photo of the gold breast cream jar with its plum lid"></div>
  <div class="product__text product__text--cream">
    <h2 class="product__name">Amber Petal Firming and Lifting Breast Cream</h2>
    <p class="product__desc">Using all natural Ayurvedic herbs, our breast cream helps enhance, tighten, and lift your breast</p>
  </div>

  <div class="product__img product__img--serum" role="img" aria-label="Photo of the gold-flake breast serum dropper bottle"></div>
  <div class="product__text product__text--serum">
    <h2 class="product__name">Amber Petal Firming and Toning Breast Serum</h2>
    <p class="product__desc">Using all natural Ayurvedic herbs, &amp; a touch of 24k gold, our serum enhances the experience and quality of results when partnered with the Amber Petal Firming &amp; Lifting Breast Cream providing an all-day boosting experience</p>
  </div>

  <div class="footer">
    <svg width="440" height="110" viewBox="0 0 440 110">
      <path d="M0 4 Q220 62 440 30 L440 110 L0 110 Z" fill="var(--gold-light)"/>
      <path d="M0 16 Q220 66 440 34 L440 110 L0 110 Z" fill="var(--plum)"/>
    </svg>
    <div class="contact" style="bottom:22px">
      <span class="phone"><svg width="16" height="16" viewBox="0 0 16 16"><circle cx="8" cy="8" r="7" fill="none" stroke="#fff" stroke-width="1.2"/><path d="M5.3 4.5l1.3 0 .5 1.6-.8.7c.4.9 1 1.5 1.9 1.9l.7-.8 1.6.5 0 1.3c-3 .3-5.5-2.2-5.2-5.2z" fill="#fff"/></svg>555 010 2040</span>
      <span><svg width="16" height="16" viewBox="0 0 16 16" fill="none" stroke="#fff" stroke-width="1.1"><circle cx="8" cy="8" r="6.5"/><ellipse cx="8" cy="8" rx="2.8" ry="6.5"/><path d="M1.5 8h13M2.5 5h11M2.5 11h11"/></svg>www.amberpetal.com</span>
    </div>
  </div>
</section>

</body>
</html>
```